NZ First of it's kind solutions directory and marketplace for busy Mums needs a business card design

We need a business card design for our new nationwide business in NZ (long term plans to go global). We provide solutions to the everyday challenges that busy Mums face by connecting them with quality communities and suppliers of carefully selected, relevant products and services. We sell direct via our online marketplace. The final design should communicate our values of inclusivity, quality and smart solutions. Colours should incorporate our logo colour palette of #477077 and #6ba8b2. Our website is at https://www.brightnestly.com

Target Market(s)

busy Mums, Age 28 – 50, female, income over $100K, location main centres NZ primarily but NZ wide. Is likely juggling work or career with a young family. Probably had hobbies which have fallen by the wayside.
-Wants to succeed in her chosen career without compromising on family life
-to successfully juggle her career without feeling like she is compromising her children
- Is time poor, something always has to give and it’s generally her health (she’ll stay up late, get stressed)
- probably ex corporate or professional career. Has discretional income

Industry/Entity Type

Business

Contact Information for Business Card

Jodie Farnsworth, Founder, BrightNestly.com (Strapline Browse; Pick; Sorted), 48 Kowhai Terrace, Hillsborough, Auckland 1058, New Zealand. Mob: 021 437 518 Ph: +64 (0)9 584 7163

Font styles to use
Other font styles liked:
• Raleway, and/or Architects Daughter

Colors
00a990
33b8a4
86cfc6
cfeae6

Requirements
Must have
• the above details, streamline. the logo and colours associated with those logos
Should not have
• foil or metallic colours

```html
<!DOCTYPE html>
<html lang="en">
<head>
<meta charset="utf-8">
<title>BrightNestly Business Card</title>
<link rel="stylesheet" href="https://fonts.googleapis.com/css2?family=Arimo:wght@400;700&display=swap">
<style>
  :root {
    --stage: #070707;
    --card-front: #ffffff;
    --teal-dark: #477077;
    --teal-light: #6ba8b2;
    --ink: #3c3c3c;
    --text: #222222;
    --rule: #cfcfcf;
    --back-a: #5a8f97;
    --back-b: #6ba8b2;
    --white: #ffffff;
  }
  * { box-sizing: border-box; margin: 0; padding: 0; }
  html, body { width: 1200px; height: 900px; overflow: hidden; background: var(--stage); }
  body { position: relative; font-family: "Arimo", Arial, sans-serif; }

  .card {
    position: absolute;
    top: 306px;
    width: 440px;
    height: 271px;
    border-radius: 10px;
    overflow: hidden;
    box-shadow: 0 2px 6px rgba(0,0,0,0.5);
  }
  .card--front { left: 149px; background: var(--card-front); }
  .card--back {
    left: 608px;
    background: radial-gradient(ellipse at 60% 45%, var(--back-b) 0%, var(--back-a) 100%);
  }

  .brand {
    position: absolute;
    display: flex;
    align-items: center;
    gap: 10px;
    font-weight: 700;
    letter-spacing: -0.5px;
    white-space: nowrap;
  }
  .brand__dot { border-radius: 50%; flex: none; }
  .card--front .brand { right: 23px; top: 72px; font-size: 33px; color: var(--teal-dark); }
  .card--front .brand__dot { width: 26px; height: 26px; background: var(--teal-dark); }
  .card--back .brand { left: 72px; top: 118px; font-size: 37px; color: var(--white); }
  .card--back .brand__dot { width: 30px; height: 30px; background: var(--white); }

  .back__halo {
    position: absolute;
    left: 28px; top: 20px;
    width: 150px; height: 150px;
    border-radius: 50%;
    background: rgba(255,255,255,0.06);
  }

  .holder { position: absolute; left: 27px; top: 155px; right: 23px; }
  .holder__name { font-size: 15px; font-weight: 700; color: var(--ink); letter-spacing: 0.3px; }
  .holder__name .first { color: var(--teal-dark); }
  .holder__role { display: flex; align-items: center; gap: 8px; font-size: 12px; color: var(--text); margin-top: 1px; }
  .holder__role::after { content: ""; flex: 1; height: 1px; background: var(--rule); margin-top: 2px; }

  .contact { position: absolute; left: 27px; top: 198px; font-size: 12.5px; color: var(--text); line-height: 16px; }
  .contact li { list-style: none; display: flex; align-items: center; gap: 3px; }
  .contact svg { width: 11px; height: 11px; fill: var(--teal-dark); }

  .address { position: absolute; right: 23px; top: 214px; text-align: right; font-size: 12.5px; line-height: 16px; color: var(--text); font-style: normal; }
</style>
</head>
<body>
  <section class="card card--front">
    <div class="brand"><span class="brand__dot"></span>BrightNestly</div>

    <div class="holder">
      <p class="holder__name"><span class="first">JODIE</span> FARNSWORTH</p>
      <p class="holder__role">Founder</p>
    </div>

    <ul class="contact">
      <li><svg viewBox="0 0 12 12" aria-hidden="true"><path d="M1 4c0-1.5 2.5-2.5 5-2.5S11 2.5 11 4v1H8.5V4h-5v1H1z M3 6h6l1.5 4.5h-9z"/></svg>021 437 518</li>
      <li><svg viewBox="0 0 12 12" aria-hidden="true"><path d="M3 0.5h6a1 1 0 0 1 1 1v9a1 1 0 0 1-1 1H3a1 1 0 0 1-1-1v-9a1 1 0 0 1 1-1zM3.3 2v7.5h5.4V2z"/></svg>+64 (0)9 584 7163</li>
      <li><svg viewBox="0 0 12 12" aria-hidden="true"><circle cx="6" cy="6" r="5"/><path d="M3 4c1 0 2 1 1.5 2S5 8 4.5 9.5M7 2c0 1 1.5 1 2 2.5S8 7 8.5 8" stroke="#fff" stroke-width="0.9" fill="none"/></svg>www.BrightNestly.com</li>
    </ul>

    <address class="address">48 Kowhai Terrace, Hillsborough<br>Auckland 1058, New Zealand</address>
  </section>

  <section class="card card--back">
    <div class="back__halo"></div>
    <div class="brand"><span class="brand__dot"></span>BrightNestly</div>
  </section>
</body>
</html>
```